New name flyer

We have just changed our business name from kR Property group to Harbour Lane. We want to distribute a flyer to the local community to inform them of the change. We are a realestate agency which focuses mainly on property management but also sales. We service from Brisbane to the Sunshine coast.

Target Market(s)

Local community

Industry/Entity Type

realestate

Requirements
Must have
• Details of name change
Nice to have
• Servicing area Brisbane and Sunshine Coast, no change in management or services we offer, and will continue pride ourselves on offering a high level of service, with the same team from the Gold to Sunshine Coast.
Should not have
• too much wording.

```html
<!DOCTYPE html>
<html lang="en">
<head>
<meta charset="utf-8">
<title>Harbour Lane – New Name Flyer</title>
<link rel="stylesheet" href="https://fonts.googleapis.com/css2?family=Montserrat:wght@400;500;600;700;800&family=Roboto:wght@400;500;700;900&display=swap">
<style>
  :root {
    --navy: #1f2f6b;
    --navy-deep: #1a285c;
    --gold: #c29a3a;
    --ink: #1d1d24;
    --grey-text: #4a4d58;
    --paper: #f4f5f7;
    --white: #ffffff;
    --sky-blue: #5f9ae6;
    --photo-frame: #e3e5ea;
  }
  * { margin: 0; padding: 0; box-sizing: border-box; }
  html, body { width: 764px; height: 1200px; overflow: hidden; background: var(--white); }
  .flyer {
    position: relative; width: 764px; height: 1200px; overflow: hidden;
    background: linear-gradient(160deg, #ffffff 0%, var(--paper) 45%, #eceef2 100%);
    font-family: "Montserrat", sans-serif;
  }
  .abs { position: absolute; }
  .photo {
    position: absolute; border: 4px solid var(--white);
    box-shadow: 0 1px 4px rgba(0,0,0,.25);
  }
  .hero-photo {
    left: 0; top: 0; width: 764px; height: 330px;
    background: linear-gradient(180deg, #8fb3dd 0%, #b9cde4 40%, #5b6f8e 70%, #3b4a66 100%);
  }
  .intro-panel {
    left: 0; top: 0; width: 224px; height: 160px;
    background: linear-gradient(135deg, rgba(95,154,230,.95), rgba(95,154,230,.55));
  }
  .intro-title {
    left: 46px; top: 46px; color: var(--white);
    font-weight: 800; font-size: 19px; line-height: 24px; letter-spacing: .3px;
  }
  .intro-band {
    left: 0; top: 130px; width: 224px; height: 28px;
    background: rgba(200,220,245,.55);
  }
  .intro-sub {
    left: 46px; top: 136px; color: var(--navy-deep);
    font-weight: 500; font-size: 14px; letter-spacing: .4px;
  }
  .houses-photo {
    left: 46px; top: 265px; width: 238px; height: 165px;
    background: linear-gradient(150deg, #f2f2f2 0%, #bfc2c7 55%, #8d9096 80%, #b8423b 100%);
  }
  .brand-name {
    left: 412px; top: 305px; color: var(--navy);
    font-family: "Roboto", sans-serif; font-weight: 700;
    font-size: 40px; line-height: 40px; letter-spacing: 1.5px;
  }
  .headline {
    left: 46px; top: 484px; font-family: "Roboto", sans-serif;
    font-size: 35px; line-height: 41px; color: var(--navy); letter-spacing: -.2px;
  }
  .headline b { font-weight: 900; }
  .headline .gold { color: var(--gold); font-weight: 900; }
  .headline .ink { color: var(--ink); }
  .meeting-photo { left: 543px; top: 511px; width: 174px; height: 200px;
    background: linear-gradient(160deg, #f4f4f5 0%, #dcdde0 50%, #8a6a4e 80%, #2e3038 100%); }
  .agent-photo { left: 543px; top: 730px; width: 174px; height: 265px;
    background: linear-gradient(180deg, #b7c4a5 0%, #8fb4d7 45%, #6aa6d8 70%, #7a9a55 100%); }
  .models-photo { left: 355px; top: 861px; width: 173px; height: 120px;
    background: linear-gradient(180deg, #9fb0c8 0%, #e9e3d8 60%, #c9b08a 100%); }
  .signing-photo { left: 355px; top: 996px; width: 173px; height: 118px;
    background: linear-gradient(160deg, #e8e9eb 0%, #c5c9cf 50%, #2a3550 100%); }
  .agent-role {
    left: 543px; top: 1002px; width: 174px; text-align: center;
    color: var(--gold); font-weight: 700; font-size: 13px;
  }
  .area-tag {
    left: 46px; top: 723px; width: 220px; height: 34px; background: var(--gold);
    color: var(--white); font-weight: 600; font-size: 20px; letter-spacing: .6px;
    padding: 4px 0 0 16px;
  }
  .area-name {
    left: 46px; top: 768px; color: var(--ink);
    font-weight: 700; font-size: 23px; letter-spacing: .5px;
  }
  .promises { left: 46px; top: 822px; list-style: none; }
  .promises li {
    display: flex; gap: 12px; align-items: center; height: 63px;
    color: var(--grey-text); font-size: 14px; line-height: 19px; letter-spacing: .3px;
    font-weight: 500;
  }
  .promises svg { flex: none; }
  .contact-tag {
    left: 46px; top: 1028px; width: 176px; height: 34px; background: var(--gold);
    color: var(--white); font-weight: 700; font-size: 20px; letter-spacing: .6px;
    padding: 4px 0 0 16px;
  }
  .phone {
    left: 46px; top: 1104px; display: flex; align-items: center; gap: 12px;
    color: var(--white); font-weight: 700; font-size: 30px; letter-spacing: .8px;
  }
  .contact-line {
    top: 1156px; display: flex; align-items: center; gap: 12px;
    color: var(--white); font-weight: 600; font-size: 15px; letter-spacing: .3px;
  }
  .web { left: 46px; }
  .mail { left: 373px; }
  .follow {
    left: 548px; top: 1082px; display: flex; align-items: center; gap: 6px;
    color: var(--ink); font-weight: 700; font-size: 11.5px;
  }
  .social { width: 26px; height: 26px; border-radius: 50%; background: var(--navy); }
  .follow-label { margin-right: 2px; padding-top: 16px; }
</style>
</head>
<body>
<main class="flyer">
  <div class="abs hero-photo" role="img" aria-label="City skyline of glass towers under a blue sky with sun flare"></div>
  <div class="abs intro-panel"></div>
  <div class="abs intro-band"></div>
  <p class="abs intro-title">PROPERTY<br>MANAGEMENT<br>AND SALES</p>
  <p class="abs intro-sub">REALESTATE AGENCY</p>

  <svg class="abs" style="left:0;top:0" width="764" height="1200" viewBox="0 0 764 1200" aria-hidden="true">
    <polygon points="0,310 40,330 380,330 380,338 0,338" fill="var(--gold)"/>
    <polygon points="0,318 30,338 764,338 764,760 0,760" fill="#f7f8fa"/>
    <polygon points="380,238 500,233 660,300 660,418 380,418" fill="var(--white)"/>
    <polygon points="700,418 764,360 764,385 725,418" fill="var(--gold)"/>
    <polygon points="660,402 700,402 700,418 660,418" fill="var(--gold)"/>
    <polygon points="0,760 764,760 764,1060 0,1060" fill="#f2f3f6"/>
    <line x1="46" y1="704" x2="531" y2="704" stroke="var(--navy)" stroke-width="4"/>
    <polyline points="529,704 529,498 716,498" fill="none" stroke="var(--navy)" stroke-width="4"/>
    <polygon points="460,702 529,702 529,640" fill="var(--gold)"/>
    <polygon points="0,1086 32,1058 380,1058 380,1133 690,1133 705,1146 764,1146 764,1200 0,1200" fill="var(--navy-deep)"/>
  </svg>

  <div class="photo houses-photo" role="img" aria-label="Rows of white model houses with one red-roofed house standing out"></div>

  <p class="abs brand-name">HARBOUR<br>LANE</p>

  <h1 class="abs headline">
    WE ARE NOW NAMED AS<br>
    <b>HARBOUR LANE</b><br>
    <b>ESTATE AGENTS</b> FROM<br>
    <span class="gold">KR PROPERTY GROUP.</span><br>
    <span class="ink">SEE YOU SOON!</span>
  </h1>

  <div class="photo meeting-photo" role="img" aria-label="Agent handing a small model house across a desk with a calculator"></div>
  <div class="photo agent-photo" role="img" aria-label="Portrait of a smiling real estate agent in a blue t-shirt outside a house"></div>
  <p class="abs agent-role">REAL ESTATE AGENT</p>

  <div class="abs area-tag">SERVICING AREA</div>
  <p class="abs area-name">BRISBANE AND SUNSHINE COAST</p>

  <ul class="abs promises">
    <li><svg width="18" height="18" viewBox="0 0 18 18"><circle cx="9" cy="9" r="7.5" fill="none" stroke="var(--navy)" stroke-width="1.4"/><polyline points="5.5,9.2 8,11.5 12.5,6.5" fill="none" stroke="var(--navy)" stroke-width="1.4"/></svg><span>No change in management or<br>services we offer</span></li>
    <li><svg width="18" height="18" viewBox="0 0 18 18"><circle cx="9" cy="9" r="7.5" fill="none" stroke="var(--navy)" stroke-width="1.4"/><polyline points="5.5,9.2 8,11.5 12.5,6.5" fill="none" stroke="var(--navy)" stroke-width="1.4"/></svg><span>We will continue pride ourselves<br>on offering a high level of service</span></li>
    <li><svg width="18" height="18" viewBox="0 0 18 18"><circle cx="9" cy="9" r="7.5" fill="none" stroke="var(--navy)" stroke-width="1.4"/><polyline points="5.5,9.2 8,11.5 12.5,6.5" fill="none" stroke="var(--navy)" stroke-width="1.4"/></svg><span>We are the same team from the<br>Gold to Sunshine Coast</span></li>
  </ul>

  <div class="photo models-photo" role="img" aria-label="Hands placing wooden model houses with location pins"></div>
  <div class="photo signing-photo" role="img" aria-label="Client signing a contract at a desk"></div>

  <div class="follow">
    <span class="follow-label">FOLLOW US:</span>
    <span class="social"></span><span class="social"></span><span class="social"></span>
  </div>

  <div class="abs contact-tag">CONTACT US</div>
  <p class="abs phone">
    <svg width="20" height="20" viewBox="0 0 24 24"><path d="M6.6 10.8a15.1 15.1 0 0 0 6.6 6.6l2.2-2.2c.3-.3.7-.4 1-.2 1.1.4 2.3.6 3.6.6.6 0 1 .4 1 1V20c0 .6-.4 1-1 1A17 17 0 0 1 3 4c0-.6.4-1 1-1h3.5c.6 0 1 .4 1 1 0 1.3.2 2.5.6 3.6.1.3 0 .7-.2 1z" fill="none" stroke="var(--white)" stroke-width="2"/></svg>
    612 4408 319
  </p>
  <p class="abs contact-line web">
    <svg width="18" height="18" viewBox="0 0 24 24"><circle cx="12" cy="12" r="10" fill="none" stroke="var(--white)" stroke-width="2"/><ellipse cx="12" cy="12" rx="4.5" ry="10" fill="none" stroke="var(--white)" stroke-width="2"/><line x1="2" y1="12" x2="22" y2="12" stroke="var(--white)" stroke-width="2"/></svg>
    www.harbourlaneagency.com
  </p>
  <p class="abs contact-line mail">
    <svg width="22" height="16" viewBox="0 0 22 16"><rect x="0" y="0" width="22" height="16" fill="var(--white)"/><polyline points="1,1 11,9 21,1" fill="none" stroke="var(--navy-deep)" stroke-width="2"/></svg>
    info@harbourlaneagency
  </p>
</main>
</body>
</html>
```